Established food business needs a new name card design

Refer to attached current name card. Would like a new professional look design with only the company name and logo without any pictures. Would like green and yellow to be included.
To include:
My name "IBRAHIM SUKRI" and hand phone number "87260413".
To delete "
"Along Brackendale Ave 8" and
"www.nur-tiwas.com.sg"
To change email to:
"tkr27@velmorix.com.sg"

```html
<!DOCTYPE html>
<html lang="en">
<head>
<meta charset="utf-8">
<title>Nur-Tiwas – Name Card</title>
<link rel="stylesheet" href="https://fonts.googleapis.com/css2?family=Itim&family=Nunito+Sans:wght@400;600&display=swap">
<style>
  :root {
    --backdrop: #cfcfcf;
    --green-dark: #0b3f2c;
    --green-mid: #14563a;
    --yellow: #f7cf16;
    --brand-yellow: #f2ea1c;
    --paper: #f7f7f7;
    --ink-green: #0f4a33;
    --ink: #1f2a25;
  }
  * { margin: 0; padding: 0; box-sizing: border-box; }
  html, body { width: 900px; height: 1200px; overflow: hidden; }
  body {
    background: radial-gradient(ellipse at center, #e9e9e9 0%, var(--backdrop) 100%);
    position: relative;
    font-family: "Nunito Sans", sans-serif;
  }
  .card {
    position: absolute;
    left: 82px;
    width: 740px;
    height: 431px;
    overflow: hidden;
    box-shadow: 0 6px 10px rgba(0,0,0,0.35);
  }
  .card--front {
    top: 127px;
    border-radius: 52px 0 52px 0;
    background: var(--paper);
  }
  .card--back {
    top: 634px;
    border-radius: 0 52px 0 52px;
    background: radial-gradient(ellipse at 50% 65%, var(--green-mid) 0%, var(--green-dark) 80%);
  }
  .card__art { position: absolute; inset: 0; }
  .brand {
    position: absolute;
    display: flex;
    align-items: center;
    gap: 18px;
  }
  .brand__dot {
    width: 26px; height: 26px;
    border-radius: 50%;
    background: var(--brand-yellow);
  }
  .brand__name {
    font-family: "Itim", sans-serif;
    font-size: 48px;
    line-height: 1;
    letter-spacing: 1px;
    color: var(--brand-yellow);
  }
  .card--front .brand { left: 58px; top: 92px; }
  .card--back .brand { left: 50%; top: 192px; transform: translateX(-50%); }
  .holder {
    position: absolute;
    right: 47px;
    top: 277px;
    font-family: "Itim", sans-serif;
    font-size: 29px;
    letter-spacing: 1px;
    color: var(--ink-green);
  }
  .divider {
    position: absolute;
    left: 51px; right: 47px;
    top: 319px;
    height: 2px;
    background: var(--ink-green);
  }
  .address {
    position: absolute;
    left: 51px;
    top: 328px;
    font-size: 17px;
    line-height: 23px;
    color: var(--ink);
    font-style: normal;
  }
  .contact {
    position: absolute;
    right: 46px;
    top: 328px;
    list-style: none;
    font-size: 17px;
    line-height: 23px;
    color: var(--ink);
    text-align: right;
  }
  .contact li { display: flex; align-items: center; justify-content: flex-end; gap: 8px; height: 24px; }
  .contact__icon {
    width: 20px; height: 20px;
    border-radius: 50%;
    background: var(--yellow);
    display: flex; align-items: center; justify-content: center;
  }
</style>
</head>
<body>

<section class="card card--front" aria-label="Name card front">
  <svg class="card__art" viewBox="0 0 740 431" width="740" height="431" aria-hidden="true">
    <defs>
      <radialGradient id="front-green" cx="0.2" cy="0.3" r="0.9">
        <stop offset="0" stop-color="#16593c"/>
        <stop offset="1" stop-color="#0b3f2c"/>
      </radialGradient>
    </defs>
    <path d="M0 0 H740 C610 150 360 235 0 240 Z" fill="url(#front-green)"/>
    <path d="M0 240 C360 235 610 150 740 0 L740 6 C630 150 390 270 0 287 Z" fill="var(--yellow)"/>
  </svg>

  <div class="brand">
    <span class="brand__dot"></span>
    <span class="brand__name">NUR-TIWAS</span>
  </div>

  <h1 class="holder">IBRAHIM SUKRI</h1>
  <div class="divider"></div>

  <address class="address">
    18 Kelvara Industrial<br>
    Estate Road 6 # 02-07<br>
    Singapore 731846
  </address>

  <ul class="contact">
    <li>
      <span>87260413</span>
      <span class="contact__icon">
        <svg width="12" height="12" viewBox="0 0 24 24" aria-hidden="true"><path fill="#0f4a33" d="M6.6 10.8a15 15 0 0 0 6.6 6.6l2.2-2.2c.3-.3.7-.4 1-.2 1.1.4 2.3.6 3.6.6.6 0 1 .4 1 1V20c0 .6-.4 1-1 1A17 17 0 0 1 3 4c0-.6.4-1 1-1h3.5c.6 0 1 .4 1 1 0 1.3.2 2.5.6 3.6.1.3 0 .7-.2 1z"/></svg>
      </span>
    </li>
    <li>
      <span>tkr27@velmorix.com.sg</span>
      <span class="contact__icon">
        <svg width="12" height="12" viewBox="0 0 24 24" aria-hidden="true"><rect x="2" y="5" width="20" height="14" rx="1" fill="#0f4a33"/><path d="M3 6l9 7 9-7" fill="none" stroke="#f7cf16" stroke-width="2"/></svg>
      </span>
    </li>
  </ul>
</section>

<section class="card card--back" aria-label="Name card back">
  <div class="brand">
    <span class="brand__dot"></span>
    <span class="brand__name">NUR-TIWAS</span>
  </div>
</section>

</body>
</html>
```